Brightholm painting

Am looking for a lawn sign design for my paintings company.
I also attached my business card a example

Phone number of the business +1(431)572-8846
Key words:Free estimates|pressure washing |Residential| Commercial | Interior | Exterior

```html
<!DOCTYPE html>
<html lang="en">
<head>
<meta charset="utf-8">
<title>Brightholm Painting – Lawn Sign</title>
<link rel="stylesheet" href="https://fonts.googleapis.com/css2?family=Poppins:wght@600;700;800&display=swap">
<style>
  :root {
    --sign-black: #060606;
    --sign-charcoal: #3a3a3a;
    --frame-white: #f4f4f2;
    --brand-teal: #4cc3b8;
    --box-green: #6cbf3d;
    --text-white: #ffffff;
    --name-yellow: #f2e21b;
    --splash-orange: #f07a1e;
    --splash-red: #e23a24;
    --splash-blue: #4fb6e6;
    --splash-purple: #8a3fb0;
    --splash-yellow: #f6d23a;
  }
  * { margin: 0; padding: 0; box-sizing: border-box; }
  html, body { width: 1200px; height: 1117px; overflow: hidden; background: #e9e9e6; }
  body { font-family: "Poppins", sans-serif; }

  .lawn-sign {
    position: relative;
    width: 1200px;
    height: 1117px;
    background: var(--frame-white);
    padding: 22px;
  }
  .sign-face {
    position: relative;
    width: 100%;
    height: 100%;
    overflow: hidden;
    background:
      radial-gradient(ellipse 420px 520px at 92% 38%, var(--sign-charcoal), transparent 70%),
      var(--sign-black);
  }

  .splash-top-left {
    position: absolute;
    left: -20px;
    top: -20px;
    width: 360px;
    height: 220px;
    background:
      radial-gradient(circle 120px at 75% 30%, var(--splash-yellow), transparent 70%),
      radial-gradient(circle 150px at 20% 40%, var(--splash-blue), transparent 72%);
    opacity: 0.9;
  }
  .splash-bottom {
    position: absolute;
    left: 0;
    right: 0;
    bottom: 0;
    height: 330px;
    background: linear-gradient(90deg, var(--splash-yellow) 0%, var(--splash-red) 14%, var(--splash-orange) 34%, #5a3a2c 52%, var(--splash-blue) 66%, var(--splash-purple) 86%, #b05bc8 100%);
    -webkit-mask-image: linear-gradient(to top, #000 45%, transparent 100%);
    mask-image: linear-gradient(to top, #000 45%, transparent 100%);
    opacity: 0.85;
  }

  .brand-name {
    position: absolute;
    top: 150px;
    left: 0;
    right: 0;
    text-align: center;
    color: var(--brand-teal);
    font-weight: 800;
    line-height: 1;
  }
  .brand-name .brand-main {
    display: block;
    font-size: 148px;
    letter-spacing: -2px;
  }
  .brand-name .brand-sub {
    display: block;
    margin-top: 22px;
    font-size: 58px;
    letter-spacing: 0.62em;
    padding-left: 0.62em;
  }

  .services {
    position: absolute;
    left: 148px;
    top: 565px;
    width: 860px;
    height: 190px;
  }
  .services-frame {
    position: absolute;
    inset: 0;
  }
  .services-list {
    position: relative;
    padding: 0 30px;
    margin-top: -22px;
    text-align: center;
    color: var(--text-white);
    font-weight: 700;
    font-size: 38px;
    line-height: 1.42;
  }

  .contact-bar {
    position: absolute;
    left: 0;
    right: 0;
    bottom: 42px;
    display: flex;
    justify-content: center;
    align-items: center;
    gap: 22px;
    color: var(--text-white);
    font-weight: 600;
    font-size: 29px;
  }
  .contact-name { color: var(--name-yellow); font-weight: 800; font-size: 36px; letter-spacing: 2px; margin-right: 18px; }
  .contact-item { display: flex; align-items: center; gap: 8px; }
  .contact-icon { width: 28px; height: 28px; }
  .contact-divider { width: 2px; height: 36px; background: var(--text-white); }
</style>
</head>
<body>
  <main class="lawn-sign">
    <div class="sign-face">
      <div class="splash-top-left" role="img" aria-label="Blue and yellow paint splash in the corner"></div>
      <div class="splash-bottom" role="img" aria-label="Rainbow paint splash band in orange, red, blue and purple"></div>

      <h1 class="brand-name">
        <span class="brand-main">BRIGHTHOLM</span>
        <span class="brand-sub">PAINTING</span>
      </h1>

      <section class="services">
        <svg class="services-frame" viewBox="0 0 860 190" preserveAspectRatio="none" aria-hidden="true">
          <polyline points="130,2 2,2 2,188 858,188 858,12 760,12" fill="none" stroke="var(--box-green)" stroke-width="4"/>
        </svg>
        <p class="services-list">Free estimates | pressure<br>washing | Residential | Commercial |<br>Interior | Exterior</p>
      </section>

      <footer class="contact-bar">
        <span class="contact-name">Marco</span>
        <span class="contact-item">
          <svg class="contact-icon" viewBox="0 0 24 24" aria-hidden="true">
            <circle cx="12" cy="12" r="12" fill="var(--text-white)"/>
            <path d="M8.2 6.5l1.8-.3 1.2 2.8-1.3 1c.7 1.5 1.8 2.6 3.3 3.3l1-1.3 2.8 1.2-.3 1.8c-.2.8-1 1.2-1.8 1-4-.9-7.2-4.1-8.1-8.1-.2-.8.2-1.6 1.4-1.4z" fill="var(--sign-black)"/>
          </svg>
          +1(431)572-8846
        </span>
        <span class="contact-divider"></span>
        <span class="contact-item">
          <svg class="contact-icon" viewBox="0 0 24 24" aria-hidden="true">
            <circle cx="12" cy="12" r="12" fill="var(--text-white)"/>
            <g fill="none" stroke="var(--sign-black)" stroke-width="1.3">
              <circle cx="12" cy="12" r="6.5"/>
              <ellipse cx="12" cy="12" rx="3" ry="6.5"/>
              <line x1="5.5" y1="12" x2="18.5" y2="12"/>
            </g>
          </svg>
          brightholmpaint@mailbox.net
        </span>
      </footer>
    </div>
  </main>
</body>
</html>
```